GuardLume website design #1 alarm company in Arizona and California

Alarm company, home security, home protection, video, home automation, smart home, we protect family we the highest quality security products in the market with 24 hour montrioning, also allow family's to control their whole house by being everywhere in the world.

In short, we’re professional, experienced and have the necessary know-how to optimally secure your home or business. Add those skills with our commitment to service and saving you money, and you can’t go wrong trusting

Looking to have a website for current customers and future customers and current employees and future employees to go to. Target current markets listed below get a lot of leads of the website.

Target Market(s)

Arizona and California, Phoenix, Mesa,Gilbert, casa grande, Arizona city, Glendale, peoria, Goodyear, Scottsdale, fountain hills, apache junction, Tempe, surprise, anthem, buckeye, Tucson, Northern California, Modesto, Fresno, Stockton, San Jose, Manteca, Tracy, Sacramento, concord, Southern California, San Bernardino, riverside, Anaheim, Los Angeles, palm desert, Bakersfield

Industry/Entity Type

Security

Coding

Coded - Design and coding required

Number of Pages Required

5+ page

Font styles to use
Sans Serif

Colors
ec1f27
f59296
ffffff
000000
b2b2b2
cacaca
fbd4d5

Requirements
Must have
• A place where a customer can put in the info to get a system(get a free quote),a link to all of my socal media sites, a work for us page, about us page, equipment page, packages page, security page, cameras page, smart home page, support page(FAQ http://www.brightvalehome.example/faq)somthing like the alomost every answer is right. Partners page.
Nice to have
• Quorlan.example, very nicely done make it look nice like this.
• Brightvalehome.example
• Pemby.example
• Tulsix.example
• Sentravox9.example
• Wexmoresecurity.example
• These are all my favorite sites would love for it to look like this sites.
Should not have
• Need to be clean cut and sharp looking, no unnecessary stuff in it.

```html
<!DOCTYPE html>
<html lang="en">
<head>
<meta charset="utf-8">
<title>GuardLume — Home Security</title>
<link rel="stylesheet" href="https://fonts.googleapis.com/css2?family=Montserrat:wght@300;400;500;600;700&family=Open+Sans:wght@400;600&display=swap">
<style>
:root{
  --red:#ec1f27;
  --red-soft:#f59296;
  --red-pale:#fbd4d5;
  --white:#ffffff;
  --black:#000000;
  --grey:#b2b2b2;
  --grey-light:#cacaca;
  --header:#2e2e2e;
  --topbar:#262626;
  --section:#f3f3f3;
  --footer:#303030;
  --text:#333333;
  --muted:#8a8a8a;
}
*{box-sizing:border-box;margin:0;padding:0}
html,body{width:1200px;height:3651px;overflow:hidden;background:var(--white)}
body{position:relative;font-family:"Open Sans",Arial,sans-serif;color:var(--text)}
.abs{position:absolute}
a{text-decoration:none}

/* header */
.topbar{left:0;top:0;width:1200px;height:54px;background:var(--topbar)}
.navbar{left:0;top:54px;width:1200px;height:68px;background:var(--header)}
.social-mini{top:12px;width:30px;height:30px;display:flex;align-items:center;justify-content:center}
.social-mini::before{content:"";width:10px;height:10px;border-radius:50%;background:#bbb}
.social-mini.active{border-bottom:3px solid var(--red)}
.social-mini.active::before{background:#888}
.login{left:242px;top:17px;color:var(--white);font:600 15px "Montserrat",sans-serif;display:flex;align-items:center;gap:8px}
.chat{left:798px;top:17px;color:var(--white);font:600 15px "Montserrat",sans-serif;display:flex;align-items:center;gap:8px}
.phone{left:955px;top:12px;color:var(--white);font:500 23px "Montserrat",sans-serif;display:flex;align-items:center;gap:12px}
.brand{left:500px;top:20px;width:200px;height:96px;display:flex;flex-direction:column;align-items:center;justify-content:flex-end}
.brand-mark{width:44px;height:44px;background:var(--red);margin-bottom:6px}
.brand-name{font:700 30px "Montserrat",sans-serif;color:var(--red);letter-spacing:-.5px}
.nav-link{top:74px;font:600 15px "Montserrat",sans-serif;color:var(--white);text-transform:uppercase}
.nav-link.active{border-bottom:2px solid var(--red);padding-bottom:6px}

/* hero */
.hero{left:0;top:122px;width:1200px;height:555px;background:linear-gradient(100deg,#cfc4bb 0%,#e9e2dc 35%,#f4f1ee 60%,#fbfaf9 100%)}
.hero-title{left:643px;top:256px;font:300 52px/60px "Montserrat",sans-serif;color:#1e1e1e}
.hero-text{left:645px;top:380px;width:480px;font:400 17px/27px "Open Sans",sans-serif;color:#333}
.btn{display:flex;align-items:center;justify-content:center;border-radius:28px;font:600 15px "Montserrat",sans-serif;text-transform:uppercase}
.btn-red{background:var(--red);color:var(--white)}
.btn-white{background:var(--white);color:var(--red)}

/* badges */
.badges{left:0;top:677px;width:1200px;height:146px;background:var(--white);box-shadow:0 6px 10px rgba(0,0,0,.12);display:flex;align-items:center;justify-content:space-around;padding:0 70px}
.badge{background:var(--grey-light)}

/* why */
.why{left:0;top:823px;width:1200px;height:540px;background:var(--section)}
.section-title{width:1200px;left:0;text-align:center;font:300 44px "Montserrat",sans-serif;color:#222}
.section-title b{font-weight:700}
.section-sub{width:1200px;left:0;text-align:center;font:400 16px/26px "Open Sans",sans-serif;color:var(--muted)}
.feature{width:360px;text-align:center}
.feature h3{font:400 23px "Montserrat",sans-serif;color:#222;margin-top:24px}
.feature p{font:400 14px/23px "Open Sans",sans-serif;color:var(--muted);margin-top:12px}

/* door */
.door{left:0;top:1266px;width:1200px;height:560px;background:var(--white);clip-path:polygon(0 14%,100% 0,100% 86%,0 100%)}
.door-photo{left:0;top:1266px;width:572px;height:560px;background:linear-gradient(120deg,#d9d2c8,#f1ede7 50%,#c9c3ba);clip-path:polygon(0 14%,100% 3%,100% 88%,0 100%)}
.door-title{left:613px;top:1410px;font:300 42px/52px "Montserrat",sans-serif;color:#222}
.door-text{left:614px;top:1532px;font:400 14px "Open Sans",sans-serif;color:#444}

/* services */
.services{left:0;top:1789px;width:1200px;height:560px;background:var(--section);z-index:-1}
.svc{width:170px;text-align:center}
.svc-circle{width:124px;height:124px;border-radius:50%;background:var(--white);margin:0 auto;box-shadow:0 2px 6px rgba(0,0,0,.08)}
.svc-circle.ring{border:4px solid var(--red)}
.svc-label{margin-top:16px;font:600 16px "Montserrat",sans-serif}
.device{left:677px;top:1850px;width:413px;height:342px;border-radius:20px;background:linear-gradient(180deg,#fbfbfb,#e9e9e9);box-shadow:0 3px 10px rgba(0,0,0,.1)}

/* reviews */
.reviews{left:0;top:2337px;width:1200px;height:377px;background:var(--white)}
.review{width:330px;text-align:center}
.quote-dot{width:40px;height:40px;border-radius:50%;background:var(--red);margin:0 auto;display:flex;align-items:center;justify-content:center;gap:4px}
.quote-dot i{display:block;width:5px;height:14px;background:var(--white);border-radius:2px}
.review p{margin-top:22px;font:400 14px/23px "Open Sans",sans-serif;color:#444}
.review h4{margin-top:14px;font:400 19px "Montserrat",sans-serif;color:#222;text-transform:uppercase}

/* quote */
.quote-bg{left:0;top:2714px;width:1200px;height:487px;background:linear-gradient(90deg,#eef0f4,#f7f8fb 60%,#ffffff)}
.quote-left{left:0;top:2714px;width:523px;height:487px;background:linear-gradient(160deg,#d3d0cb,#bdb8b2 60%,#a9a49e)}
.panel{left:116px;top:2875px;width:318px;height:222px;border-radius:14px;background:linear-gradient(135deg,#7fb8a0,#4d8f7a)}
.quote-kicker{left:755px;top:2808px;width:311px;text-align:center;font:500 20px "Montserrat",sans-serif;color:#222}
.quote-title{left:730px;top:2834px;width:360px;text-align:center;font:600 56px/66px "Montserrat",sans-serif;color:var(--red)}
.field{left:755px;width:311px;height:48px;border-radius:24px;background:var(--white);border:1px solid var(--grey-light);font:400 15px "Open Sans",sans-serif;color:#666;padding-left:28px;display:flex;align-items:center}

/* footer */
.footer{left:0;top:3201px;width:1200px;height:333px;background:var(--footer)}
.fcol h5{font:400 21px "Montserrat",sans-serif;color:var(--white);margin-bottom:20px}
.fcol li{list-style:none;font:400 14px "Open Sans",sans-serif;color:#ddd;margin-bottom:15px}
.fcol li::before{content:"» "}
.partner-box{width:187px;height:98px;background:var(--white);display:flex;align-items:center;justify-content:center;gap:10px;font:700 17px "Montserrat",sans-serif;color:#222}
.partner-box .sq{width:26px;height:26px;background:#222}
.fcol .follow li{display:flex;align-items:center;gap:12px;margin-bottom:13px}
.fcol .follow li::before{content:"";width:26px;height:26px;border-radius:50%;background:var(--red);flex:none}
.fcol .follow li.light::before{background:#e8e8e8}
.copy{left:0;top:3534px;width:1200px;height:117px;background:var(--red);display:flex;align-items:center;justify-content:center;font:600 15px "Montserrat",sans-serif;color:#2a0000}
</style>
</head>
<body>

<!-- header -->
<div class="abs topbar"></div>
<div class="abs navbar"></div>
<div class="abs social-mini" style="left:70px"></div>
<div class="abs social-mini" style="left:118px"></div>
<div class="abs social-mini active" style="left:168px"></div>
<div class="abs login">
  <svg width="16" height="12" viewBox="0 0 16 12"><rect width="16" height="12" rx="2" fill="#ec1f27"/></svg>LOGIN / SIGN UP
</div>
<div class="abs chat">
  <svg width="22" height="18" viewBox="0 0 22 18"><path d="M3 2h16a2 2 0 0 1 2 2v8a2 2 0 0 1-2 2H9l-5 4v-4H3a2 2 0 0 1-2-2V4a2 2 0 0 1 2-2z" fill="none" stroke="#ec1f27" stroke-width="2"/></svg>Chat with Us
</div>
<div class="abs phone">
  <svg width="22" height="22" viewBox="0 0 24 24"><path d="M6.6 10.8a15 15 0 0 0 6.6 6.6l2.2-2.2a1 1 0 0 1 1-.25 11.4 11.4 0 0 0 3.6.57 1 1 0 0 1 1 1V20a1 1 0 0 1-1 1A17 17 0 0 1 3 4a1 1 0 0 1 1-1h3.5a1 1 0 0 1 1 1c0 1.25.2 2.45.57 3.57a1 1 0 0 1-.25 1z" fill="#ec1f27"/></svg>480-210-7734
</div>
<div class="abs brand">
  <div class="brand-mark"></div>
  <div class="brand-name">GuardLume</div>
</div>
<div class="abs nav-link active" style="left:168px">Home</div>
<div class="abs nav-link" style="left:265px">About</div>
<div class="abs nav-link" style="left:368px">Services</div>
<div class="abs nav-link" style="left:758px">Products</div>
<div class="abs nav-link" style="left:892px">Support</div>
<div class="abs nav-link" style="left:1013px">Contact</div>

<!-- hero -->
<div class="abs hero" role="img" aria-label="Photo of a child sleeping peacefully hugging a soft toy"></div>
<h1 class="abs hero-title">Feel Secure &amp; Safe<br>With GuardLume</h1>
<p class="abs hero-text">Lorem Ipsum is simply dummy text of the printing and typesetting industry. Lorem Ipsum has been the industry's standard.</p>
<a class="abs btn btn-red" style="left:642px;top:484px;width:168px;height:54px">Get Started</a>
<a class="abs btn btn-white" style="left:829px;top:484px;width:188px;height:54px">Request Quote</a>

<!-- trust badges -->
<div class="abs badges">
  <div class="badge" style="width:138px;height:30px;border-radius:4px"></div>
  <div class="badge" style="width:50px;height:90px;border-radius:4px"></div>
  <div class="badge" style="width:78px;height:78px;border-radius:50%"></div>
  <div class="badge" style="width:96px;height:34px;border-radius:4px"></div>
  <div class="badge" style="width:64px;height:64px;border-radius:50%"></div>
  <div class="badge" style="width:118px;height:48px;border-radius:4px"></div>
  <div class="badge" style="width:112px;height:42px;border-radius:4px"></div>
</div>

<!-- why -->
<div class="abs why"></div>
<h2 class="abs section-title" style="top:870px">Why People Like <b>GUARDLUME?</b></h2>
<p class="abs section-sub" style="top:934px">Lorem Ipsum is simply dummy text of the printing and typesetting industry.<br>Lorem Ipsum has been the industry's standard.</p>

<div class="abs feature" style="left:115px;top:1030px">
  <svg width="96" height="90" viewBox="0 0 96 90" fill="none" stroke="#ec1f27" stroke-width="3"><rect x="18" y="12" width="66" height="28" rx="4" transform="rotate(18 51 26)"/><path d="M32 44l-6 18H8M8 54v16"/><circle cx="72" cy="36" r="4"/></svg>
  <h3>Security &amp; Surveillance</h3>
  <p>Wireless home security and<br>24×7 continuous video recording</p>
</div>
<div class="abs feature" style="left:420px;top:1030px">
  <svg width="96" height="90" viewBox="0 0 96 90" fill="none" stroke="#ec1f27" stroke-width="3"><rect x="32" y="8" width="32" height="74" rx="5"/><rect x="38" y="16" width="20" height="14"/><circle cx="42" cy="42" r="2"/><circle cx="54" cy="42" r="2"/><circle cx="42" cy="54" r="2"/><circle cx="54" cy="54" r="2"/><circle cx="42" cy="66" r="2"/><circle cx="54" cy="66" r="2"/></svg>
  <h3>Smart Home Control</h3>
  <p>Receive notifications and control your<br>smart home system from anywhere</p>
</div>
<div class="abs feature" style="left:713px;top:1030px">
  <svg width="96" height="90" viewBox="0 0 96 90" fill="none" stroke="#ec1f27" stroke-width="3"><circle cx="48" cy="40" r="22"/><path d="M22 40a26 26 0 0 1 52 0M22 36v12M74 36v12M74 48c0 12-10 18-20 18"/><path d="M26 86c2-10 10-16 22-16s20 6 22 16"/></svg>
  <h3>24x7 Monitoring</h3>
  <p>Smart Home Specialists are always<br>there to respond to an emergency</p>
</div>

<!-- services background -->
<div class="abs services"></div>

<!-- door -->
<div class="abs door"></div>
<div class="abs door-photo" role="img" aria-label="Photo of a couple relaxing on a white sofa with a tablet"></div>
<h2 class="abs door-title">We’re coming to your<br>door.</h2>
<p class="abs door-text">Lorem Ipsum is simply dummy text of the printing and typesetting industry.</p>
<a class="abs btn btn-red" style="left:614px;top:1582px;width:156px;height:50px">Reach Us</a>

<!-- services -->
<h2 class="abs section-title" style="top:1794px;width:820px;left:0"><b>Services</b> We Provide</h2>
<div class="abs svc" style="left:204px;top:1870px">
  <div class="svc-circle ring" role="img" aria-label="Doorbell camera product photo" style="background:radial-gradient(circle,#bfbfbf 0 30%,#e4e4e4 31%)"></div>
  <div class="svc-label" style="color:#222">Doorbell Camera</div>
</div>
<div class="abs svc" style="left:419px;top:1870px">
  <div class="svc-circle" role="img" aria-label="Outdoor camera product photo" style="background:radial-gradient(circle,#dcdcdc 0 35%,#fff 36%)"></div>
  <div class="svc-label" style="color:var(--red)">Outdoor Camera</div>
</div>
<div class="abs svc" style="left:204px;top:2068px">
  <div class="svc-circle" role="img" aria-label="Life alert pendant product photo" style="background:radial-gradient(circle,#c9c9c9 0 30%,#fff 31%)"></div>
  <div class="svc-label" style="color:var(--red)">Life Alert</div>
</div>
<div class="abs svc" style="left:419px;top:2068px">
  <div class="svc-circle" role="img" aria-label="Smart lock keypad product photo" style="background:radial-gradient(circle,#3a3a3a 0 28%,#fff 29%)"></div>
  <div class="svc-label" style="color:var(--red)">Smart Locks</div>
</div>
<div class="abs device" role="img" aria-label="Smart thermostat product photo"></div>

<!-- reviews -->
<div class="abs reviews"></div>
<h2 class="abs section-title" style="top:2325px">Customer <b>Reviews</b></h2>
<div class="abs badge" style="left:376px;top:2400px;width:200px;height:72px;border-radius:6px"></div>
<div class="abs badge" style="left:622px;top:2400px;width:216px;height:72px;border-radius:6px"></div>

<div class="abs review" style="left:64px;top:2511px">
  <div class="quote-dot"><i></i><i></i></div>
  <p>" Lorem Ipsum is simply dummy text of the printing and typesetting industry. Lorem Ipsum has been the industry's standard."</p>
  <h4>Jon Dorey</h4>
</div>
<div class="abs review" style="left:420px;top:2511px">
  <div class="quote-dot"><i></i><i></i></div>
  <p>" Lorem Ipsum is simply dummy text of the printing and typesetting industry. Lorem Ipsum has been the industry's standard."</p>
  <h4>Kara Wendell</h4>
</div>
<div class="abs review" style="left:778px;top:2511px">
  <div class="quote-dot"><i></i><i></i></div>
  <p>" Lorem Ipsum is simply dummy text of the printing and typesetting industry. Lorem Ipsum has been the industry's standard."</p>
  <h4>Stan Belkin</h4>
</div>

<!-- quote -->
<div class="abs quote-bg" role="img" aria-label="Soft photo of a bright modern interior"></div>
<div class="abs quote-left" role="img" aria-label="Photo of a wall-mounted security touch panel"></div>
<div class="abs panel" role="img" aria-label="Security touch panel screen"></div>
<div class="abs quote-kicker">LET'S GET STARTED!</div>
<h2 class="abs quote-title">Get a Quote</h2>
<div class="abs field" style="top:2920px">Name</div>
<div class="abs field" style="top:2976px">Phone</div>
<div class="abs field" style="top:3032px">E-mail</div>
<a class="abs btn btn-red" style="left:755px;top:3096px;width:311px;height:52px;text-transform:none;font-size:21px;font-weight:500">Request a Quote</a>

<!-- footer -->
<div class="abs footer"></div>
<div class="abs fcol" style="left:78px;top:3236px">
  <h5>Support</h5>
  <ul><li>Contact Us</li><li>One Resources</li><li>Military Families</li><li>Corporate Blog</li><li>Licence</li></ul>
</div>
<div class="abs fcol" style="left:304px;top:3236px">
  <h5>Company</h5>
  <ul><li>About</li><li>Career</li><li>News</li><li>Our Locations</li><li>Leadership</li></ul>
</div>
<div class="abs fcol" style="left:526px;top:3236px">
  <h5>Partner</h5>
  <ul><li>Internet</li><li>Solar</li><li>GuardLume</li><li>GuardLume</li></ul>
</div>
<div class="abs fcol" style="left:747px;top:3236px">
  <h5>Powered by :</h5>
  <div class="partner-box"><span class="sq"></span>Hollice.example</div>
</div>
<div class="abs fcol" style="left:971px;top:3236px">
  <h5>Follow Us On</h5>
  <ul class="follow">
    <li>Fablet</li><li>Chirpline</li><li>Linkora</li><li>Streamly</li><li class="light">Rateyard</li><li class="light">Circlenet</li>
  </ul>
</div>
<div class="abs copy">© GuardLume - 2016. All Rights Reserved.</div>

</body>
</html>
```